Family Ranch with a hobby vineyard needs 2 wine labels for our first harvest

Design 2 wine labels (front and back) with the Brindor Ranch logo.
Label 1:
Sauvignon Blanc
Alc. 12.5% by Vol.
Palos Verdes Peninsula - add as the region
Year 2022
Label 2:
Cabernet Sauvignon
Alc. 13.5% by Vol.
Year 2022
For the back label design:
GOVERNMENT WARNING: (1) According to the Surgeon General, women
should not drink alcoholic beverages during pregnancy because of the risk of
birth defects. (2) Consumption of alcoholic beverages impairs your ability to
drive a car or operate machinery, and may cause health problems.
Contains Sulfates.
750ML
I just received the bottles and have attached a picture.
Look and feel
Each slider illustrates characteristics of the customer's brand and the style your logo design should communicate.

```html
<!DOCTYPE html>
<html lang="en">
<head>
<meta charset="utf-8">
<title>Brindor Ranch – Sauvignon Blanc Labels</title>
<link rel="stylesheet" href="https://fonts.googleapis.com/css2?family=Cinzel:wght@600&family=Pinyon+Script&family=EB+Garamond:wght@400;600&display=swap">
<style>
  :root {
    --backdrop: #d6cdbb;
    --paper: #e9e0cd;
    --paper-edge: #d9ceb6;
    --wine: #7b2c38;
    --ink: #2a2224;
    --ink-soft: #5a4e48;
    --ornament: #9a4a55;
  }
  * { box-sizing: border-box; margin: 0; padding: 0; }
  html, body {
    width: 1200px; height: 1200px; overflow: hidden;
    background: var(--backdrop);
  }
  .canvas {
    width: 1200px; height: 1200px;
    display: flex; align-items: center; justify-content: center; gap: 80px;
  }
  .label {
    width: 440px; height: 600px;
    background: var(--paper);
    box-shadow: 0 0 0 1px var(--paper-edge);
    position: relative;
  }

  /* Front label */
  .front-label {
    display: flex; flex-direction: column; align-items: center;
    padding-top: 60px;
  }
  .brand {
    display: flex; flex-direction: column; align-items: center; gap: 8px;
  }
  .brand-mark {
    width: 44px; height: 44px; border-radius: 50%;
    border: 3px solid var(--wine);
  }
  .brand-name {
    font-family: "EB Garamond", serif; font-weight: 600;
    font-size: 20px; letter-spacing: 3px; color: var(--wine);
    text-transform: uppercase;
  }
  .ornament {
    width: 120px; height: 22px; border-radius: 11px;
    background: linear-gradient(90deg, transparent, var(--ornament), transparent);
    opacity: .75;
  }
  .ornament-top { margin-top: 52px; }
  .wine-name {
    margin-top: 14px; text-align: center; line-height: 1;
  }
  .varietal {
    display: block;
    font-family: "Cinzel", serif; font-weight: 600;
    font-size: 54px; color: var(--wine); letter-spacing: 1px;
  }
  .varietal-sub {
    display: block; margin-top: -10px; margin-left: 90px;
    font-family: "Pinyon Script", cursive;
    font-size: 50px; color: var(--ink);
  }
  .ornament-bottom { margin-top: 14px; }
  .details {
    margin-top: auto; margin-bottom: 56px; text-align: center;
    font-family: "EB Garamond", serif; font-size: 15px;
    letter-spacing: 1px; color: var(--ink-soft); line-height: 1.5;
    text-transform: uppercase;
  }

  /* Back label */
  .back-label {
    border: 16px solid var(--wine);
    padding: 56px 44px 44px;
    display: flex; flex-direction: column; align-items: center;
    font-family: "EB Garamond", serif; color: var(--ink);
    text-align: center;
  }
  .warning {
    font-size: 19px; line-height: 1.55;
  }
  .warning-title { font-weight: 600; letter-spacing: 1px; }
  .sulfites { margin-top: 28px; font-size: 19px; }
  .volume {
    margin-top: auto; font-size: 20px; letter-spacing: 2px; font-weight: 600;
  }
</style>
</head>
<body>
  <main class="canvas">
    <section class="label front-label" aria-label="Front label">
      <div class="brand">
        <span class="brand-mark"></span>
        <span class="brand-name">Brindor Ranch</span>
      </div>
      <div class="ornament ornament-top" role="img" aria-label="Decorative flourish"></div>
      <h1 class="wine-name">
        <span class="varietal">SAUVIGNON</span>
        <span class="varietal-sub">Blanc</span>
      </h1>
      <div class="ornament ornament-bottom" role="img" aria-label="Decorative flourish"></div>
      <p class="details">
        Alc. 12.5% by Vol.<br>
        Palos Verdes Peninsula<br>
        Year 2022
      </p>
    </section>

    <section class="label back-label" aria-label="Back label">
      <p class="warning">
        <span class="warning-title">GOVERNMENT WARNING:</span>
        (1) According to the Surgeon General, women should not drink alcoholic
        beverages during pregnancy because of the risk of birth defects.
        (2) Consumption of alcoholic beverages impairs your ability to drive a
        car or operate machinery, and may cause health problems.
      </p>
      <p class="sulfites">Contains Sulfates.</p>
      <p class="volume">750ML</p>
    </section>
  </main>
</body>
</html>
```